Verdanix Medical Business Card

Create a high class Business card for Medical Aesthetics and Wellness Practice called Verdanix Medical Aesthetics and Wellness as per the logo attached.
Addresss is: 418 Harlan Brook Road Suite 312 Melville, New York 11093
Phone (555)204-7391 IG @verdanix_medical
Verdanixmedical.example

I need 5 different name configurations
1) Dr. Theo Valcourt
Aesthetics and Wellness Specialist
Medical Director

2) Rosalind Pettinger, NP
Clinical Nurse Manager

3) Marla Vostrik, RN
Aesthetic Nurse Specialist

4) Petra Halvesen, RN

5) Dana Kowbeck, L.E.
Senior Licensed Esthetician

Target Market(s)

22-55 Females

Industry/Entity Type

Medical Spa and Wellness

Contact Information for Business Card

Logo, address, phone, web, instagram, providers name

Requirements
Must have
• Attractive classy modern look

```html
<!DOCTYPE html>
<html lang="en">
<head>
<meta charset="utf-8">
<title>Verdanix Medical Business Card</title>
<link href="https://fonts.googleapis.com/css2?family=Cormorant+Garamond:wght@400;500&family=Arimo:wght@400&display=swap" rel="stylesheet">
<style>
  :root {
    --page: #e9ecec;
    --teal: #0f4b5b;
    --teal-raised: #1a6577;
    --ink: #0f4b5b;
    --grey-text: #555b5e;
    --rule: #c9cccd;
    --paper: #ffffff;
  }
  * { box-sizing: border-box; margin: 0; padding: 0; }
  html, body { width: 1200px; height: 874px; overflow: hidden; }
  body {
    background: var(--page);
    display: flex;
    flex-direction: column;
    align-items: center;
    justify-content: center;
    gap: 34px;
  }
  .card {
    width: 665px;
    height: 380px;
    border-radius: 24px;
    position: relative;
    box-shadow: 0 6px 18px rgba(0,0,0,0.12);
  }
  .card-front {
    background: var(--teal);
    display: flex;
    align-items: center;
    justify-content: center;
  }
  .wordmark { text-align: center; font-family: "Cormorant Garamond", serif; }
  .wordmark-name {
    font-size: 74px;
    font-weight: 400;
    letter-spacing: 6px;
    line-height: 1;
  }
  .wordmark-tagline {
    font-size: 17px;
    letter-spacing: 1px;
    text-transform: uppercase;
    margin-top: 8px;
  }
  .wordmark-city {
    font-size: 11px;
    letter-spacing: 9px;
    text-transform: uppercase;
    margin-top: 8px;
  }
  .card-front .wordmark { color: var(--teal-raised); }
  .card-back { background: var(--paper); }
  .card-back .wordmark {
    position: absolute;
    left: 40px;
    top: 38px;
    color: var(--ink);
  }
  .card-back .wordmark-name { font-size: 56px; letter-spacing: 4px; }
  .card-back .wordmark-tagline { font-size: 14px; }
  .card-back .wordmark-city { font-size: 9px; letter-spacing: 7px; }
  .divider {
    position: absolute;
    left: 40px;
    right: 40px;
    top: 236px;
    border-top: 1px solid var(--rule);
  }
  .contact {
    position: absolute;
    left: 40px;
    top: 196px;
    list-style: none;
    font-family: "Arimo", sans-serif;
    font-size: 15px;
    color: var(--grey-text);
    line-height: 20px;
  }
  .contact li { display: flex; align-items: center; gap: 8px; }
  .contact svg { width: 13px; height: 13px; flex: none; fill: var(--ink); }
  .person {
    position: absolute;
    right: 40px;
    top: 190px;
    text-align: right;
  }
  .person-name {
    font-family: "Cormorant Garamond", serif;
    font-size: 30px;
    font-weight: 500;
    color: var(--ink);
    line-height: 1.1;
  }
  .person-title {
    font-family: "Arimo", sans-serif;
    font-size: 15px;
    color: var(--grey-text);
    margin-top: 18px;
  }
  .address {
    font-family: "Arimo", sans-serif;
    font-style: normal;
    font-size: 16px;
    color: #333;
    line-height: 20px;
    margin-top: 22px;
  }
</style>
</head>
<body>
  <section class="card card-front">
    <div class="wordmark">
      <div class="wordmark-name">verdanix</div>
      <div class="wordmark-tagline">Medical Aesthetics and Wellness</div>
      <div class="wordmark-city">New York</div>
    </div>
  </section>

  <section class="card card-back">
    <div class="wordmark">
      <div class="wordmark-name">verdanix</div>
      <div class="wordmark-tagline">Medical Aesthetics and Wellness</div>
      <div class="wordmark-city">New York</div>
    </div>

    <div class="divider"></div>

    <ul class="contact">
      <li>
        <svg viewBox="0 0 16 16" aria-hidden="true"><path d="M3.6 1.2l2.3 2.6-1.3 1.8c.9 2 2.6 3.7 4.6 4.6l1.8-1.3 2.6 2.3-1.3 2.4C7 13.4 2.6 9 1.2 2.5z"/></svg>
        (555)204-7391
      </li>
      <li>
        <svg viewBox="0 0 16 16" aria-hidden="true"><circle cx="8" cy="8" r="7" fill="none" stroke="currentColor" stroke-width="1.6" style="stroke:var(--ink)"/><path d="M1 8h14M8 1c-3 3.5-3 10.5 0 14M8 1c3 3.5 3 10.5 0 14" fill="none" style="stroke:var(--ink)" stroke-width="1.2"/></svg>
        Verdanixmedical.example
      </li>
      <li>
        <svg viewBox="0 0 16 16" aria-hidden="true"><rect x="1" y="1" width="14" height="14" rx="2"/></svg>
        @verdanix_medical
      </li>
    </ul>

    <div class="person">
      <div class="person-name">Rosalind Pettinger, NP</div>
      <div class="person-title">Clinical Nurse Manager</div>
      <address class="address">
        418 Harlan Brook Road<br>
        Suite 312<br>
        Melville, New York 11093
      </address>
    </div>
  </section>
</body>
</html>
```